San Francisco Leading Consulting firm - Quorvane Web Design Project

•Create a Web Design
•Uncoded webpage layout design
•2 Pages Design - Homepage + Interior Page

Task Description
Hello, we're looking for a re-design our current website www.quorvane-example.com

we have a sample mockup design @

http://quorvane.pubmirrex-example.org/

This shows the layout that we like and also a sample of 6 pictures that would change based on where you mouse over..

6 pictures HOME design needs to be included.

SMART
THOUGHTFUL
FLEXIBLE
CREATIVE SERVICES
TECHNICAL SERVICES
PARTNERS

sites we like:

http://www.belvantoadvisory-example.com/Home.cfm?id=Home
http://www.plumstudioworks-example.com/index.html

Our company can be best described as: 100+ employees, cutting-edge, depandable, innovative, strong, smart.

Our Primary focus is: IT Consulting Services and Creative Design services

Quorvane LLC is a consulting firm providing creative design, business and technology solutions to both private and public interests.

Established in 1996, Quorvane is a San Francisco based company providing specialists for a range of business needs including:

Creative Design Services
•Print
•Logo Design
•Website Design
•Illustration

and

Business and Technology solutions

•Application Software and Web Development
•Business Process Re-Design (BPR)
•Business/Systems Analysis and Requirement Documentation
•Mentoring and Training
•Network/Hardware Installation Services
•System Design and Architecture
•Vendor Management
•Sharepoint Architecture and Implementation

our sample mockup site:

Reason: Due to holiday season, we're not available to work with designers and finilize our design.  

Thank you very much for submitting your design.

We appreciate your time and creativity.   Since, our office is currently closed for holidays, we will be reviewing it in details next week and will make our decision as soon as possible.

It would be great if you could submit any of your changes by Wed next week, so it would be part of our reviews. 

Please see updated wireframe under attachments:  we have some minor updates to our wireframe that we would like you to update your designs, if possible.  

We also encorouge you not to use our standard wireframe and come up with more unique designs.   Everything would be considered when we review your design.

 

Target Market(s)

Creative services and professional services clients, including government agencies

Industry/Entity Type

Business

Requirements
Must have
• Clean, professional look, easy navigation

```html
<!DOCTYPE html>
<html lang="en">
<head>
<meta charset="utf-8">
<title>Quorvane</title>
<link rel="stylesheet" href="https://fonts.googleapis.com/css2?family=Oswald:wght@300;400&display=swap">
<style>
:root{
  --blue:#2a8ac8;
  --line:#d6e4ee;
  --text:#555;
  --muted:#666;
  --olive:#8a9a16;
  --olive-dark:#6f7d0c;
  --nav-active:#e8f4fb;
}
*{margin:0;padding:0;box-sizing:border-box}
html,body{width:1200px;height:730px;overflow:hidden;background:#fff}
body{position:relative;font-family:Arial,Helvetica,sans-serif;color:var(--text)}

.brand{position:absolute;left:224px;top:18px;display:flex;align-items:center;gap:10px}
.brand-dot{width:34px;height:34px;border-radius:50%;background:var(--blue)}
.brand-name{font-family:'Oswald',sans-serif;font-weight:300;font-size:22px;letter-spacing:2px;color:#333}

.nav{position:absolute;left:440px;top:0;height:78px;display:flex;border-right:1px solid var(--line);border-bottom:1px solid var(--line);border-bottom-right-radius:6px}
.nav a{display:block;height:78px;line-height:76px;padding:0 10px;border-left:1px solid var(--line);color:var(--blue);text-decoration:none;font-family:'Oswald',sans-serif;font-weight:300;font-size:13px;text-align:center;white-space:nowrap}
.nav a.active{background:var(--nav-active);position:relative}
.nav a.active::after{content:"";position:absolute;left:50%;bottom:-6px;margin-left:-7px;border:7px solid transparent;border-top:6px solid var(--nav-active);border-bottom:0}

.stage{position:absolute;left:216px;top:79px;width:760px;height:340px;border:1px solid var(--line);border-top:0;border-radius:0 0 0 8px}
.hero{position:absolute;left:224px;top:87px;width:752px;height:274px;border-radius:8px;background:linear-gradient(90deg,#2d3a4a 0%,#8fb8d4 30%,#cfe6f3 55%,#b9dcef 80%,#a7d1ea 100%)}
.hero-dots{position:absolute;left:232px;top:94px;display:flex;gap:7px}
.hero-dots span{width:12px;height:12px;border-radius:50%;background:rgba(255,255,255,.75)}
.hero-title{position:absolute;left:570px;top:94px;color:#fff;font-family:'Oswald',sans-serif;font-weight:300;font-size:52px;line-height:56px;letter-spacing:-1px;white-space:nowrap;text-shadow:1px 1px 2px rgba(0,0,0,.35)}
.hero-sub{position:absolute;left:570px;top:148px;width:315px;color:#fff;font-family:'Oswald',sans-serif;font-weight:300;font-size:24px;line-height:24px;text-shadow:1px 1px 2px rgba(0,0,0,.35)}

.thumb{position:absolute;top:369px;width:112px;height:40px;border-radius:5px;border:1px solid #c9c9c9;background:linear-gradient(90deg,#8d8c86 0%,#b6b4ac 35%,#d4d3ce 100%);display:flex;align-items:center;justify-content:flex-end;padding-right:16px;font-family:'Oswald',sans-serif;font-weight:300;font-size:13px;line-height:12px;color:#222;text-align:left}
.thumb.on{background:linear-gradient(90deg,#8aa5b8 0%,#c6dceb 40%,#e3f0f8 100%);border-color:#b6d2e4}
.pointer{position:absolute;left:405px;top:362px;border:6px solid transparent;border-bottom:7px solid #a9c9de;border-top:0}

.col{position:absolute;top:418px;height:167px;border:1px solid var(--line);border-radius:6px}
.col h2{position:absolute;left:16px;top:8px;color:var(--blue);font-family:'Oswald',sans-serif;font-weight:300;font-size:16px;white-space:nowrap}
.col .photo{position:absolute;left:17px;top:40px;width:72px;height:120px;border:2px solid #e3e3e3;border-radius:5px}
.col h3{position:absolute;left:107px;top:42px;font-size:12px;font-weight:bold;color:#555;white-space:nowrap;letter-spacing:-.2px}
.col p{position:absolute;left:108px;top:66px;font-size:10px;line-height:16.8px;color:var(--muted);white-space:nowrap}

.more{position:absolute;top:596px;width:84px;height:18px;border-radius:9px;background:linear-gradient(var(--olive),var(--olive-dark));color:#fff;font-family:'Oswald',sans-serif;font-weight:300;font-size:10.5px;line-height:18px;padding-left:8px;text-decoration:none}
.more::after{content:"";position:absolute;right:0;top:0;width:18px;height:18px;border-left:1px solid rgba(255,255,255,.35)}
.more svg{position:absolute;right:6px;top:5px}

.footer{position:absolute;left:224px;top:658px;width:752px;border-top:1px solid #e5e5e5;text-align:center;padding-top:6px;font-family:'Oswald',sans-serif;font-weight:300;font-size:10px;color:#555}
</style>
</head>
<body>
<div class="brand"><span class="brand-dot"></span><span class="brand-name">QUORVANE</span></div>

<nav class="nav">
  <a href="#" style="width:55px">HOME</a>
  <a href="#" class="active" style="width:70px">COMPANY</a>
  <a href="#" style="width:125px">TECHNICAL SERVICES</a>
  <a href="#" style="width:119px">CREATIVE SERVICES</a>
  <a href="#" style="width:73px">PARTNERS</a>
  <a href="#" style="width:93px">CONTACT US</a>
</nav>

<div class="stage"></div>
<div class="hero" role="img" aria-label="Support agent with headset at a laptop in a bright office"></div>
<div class="hero-dots"><span></span><span></span><span></span><span></span><span></span><span></span></div>
<div class="hero-title">TECHNICAL SERVICES</div>
<div class="hero-sub">Suspendisse a pellentesque dui, non felis.</div>

<div class="pointer"></div>
<div class="thumb" style="left:224px" role="img" aria-label="Man in front of a chalkboard">SMART</div>
<div class="thumb" style="left:352px" role="img" aria-label="Person working at a desk">FLEXIBLE</div>
<div class="thumb" style="left:479px" role="img" aria-label="Person in thought">THOUGHTFUL</div>
<div class="thumb" style="left:608px" role="img" aria-label="Team meeting">CREATIVE<br>SERVICES</div>
<div class="thumb on" style="left:736px" role="img" aria-label="Support agent">TECHNICAL<br>SERVICES</div>
<div class="thumb" style="left:863px" role="img" aria-label="Man in front of a chalkboard">SMART</div>

<section class="col" style="left:216px;width:254px">
  <h2>FOR GRAPHIC DESIGNERS</h2>
  <div class="photo" role="img" aria-label="Designer sitting in a cardboard box" style="background:linear-gradient(#1a1c20,#4a4a4a 60%,#b08a5a)"></div>
  <h3>Get Creative!</h3>
  <p>Quorvane is looking for top<br>creative talent to deliver graphic<br>design solutions for some<br>leading global brands Do you<br>have what it takes?</p>
</section>
<section class="col" style="left:470px;width:259px">
  <h2>FOR CLIENTS</h2>
  <div class="photo" role="img" aria-label="Business people in a meeting" style="background:linear-gradient(#c9d4dc,#8898a6 60%,#e9e6e0)"></div>
  <h3>The Quorvane Difference</h3>
  <p>Smart, Flexible, Thoughtful: find<br>out why leading corporations<br>and government agencies are<br>turning to Quorvane to help<br>manage their most demanding<br>IT services challenges.</p>
</section>
<section class="col" style="left:729px;width:247px">
  <h2>FOR PARTNERS</h2>
  <div class="photo" role="img" aria-label="Two business partners shaking hands" style="background:linear-gradient(#c8d6e0,#6f7c88 60%,#3b4450)"></div>
  <h3>Team Up With the Best</h3>
  <p>When it comes to technology<br>partnerships, our mission it so<br>make you a success.</p>
</section>

<a class="more" href="#" style="left:386px">LEARN MORE<svg width="6" height="8" viewBox="0 0 6 8"><path d="M1 1l3 3-3 3" stroke="#fff" fill="none" stroke-width="1.2"/></svg></a>
<a class="more" href="#" style="left:645px">LEARN MORE<svg width="6" height="8" viewBox="0 0 6 8"><path d="M1 1l3 3-3 3" stroke="#fff" fill="none" stroke-width="1.2"/></svg></a>
<a class="more" href="#" style="left:892px">LEARN MORE<svg width="6" height="8" viewBox="0 0 6 8"><path d="M1 1l3 3-3 3" stroke="#fff" fill="none" stroke-width="1.2"/></svg></a>

<footer class="footer">Copyright 2010, Quorvane, LLC All rights reserved.</footer>
</body>
</html>
```